New homepage and Product page - Meadow Vy

Reason: I have narrowed it done to 3 designers and just need to get the designs revised

Industry/Entity Type

Product

```html
<!DOCTYPE html>
<html lang="en">
<head>
<meta charset="utf-8">
<title>Meadow Vy – Home</title>
<link rel="stylesheet" href="https://fonts.googleapis.com/css2?family=Roboto+Condensed:wght@400;700&family=Roboto:wght@400;700&display=swap">
<style>
  :root {
    --brand-green: #1f6b2f;
    --accent-green: #6dba45;
    --rule-green: #76b957;
    --hero-dark: #1e5a22;
    --hero-mid: #3f8a36;
    --hero-light: #79b06a;
    --trust-yellow: #f6dc00;
    --pill-green: #b8dba0;
    --pill-border: #e4f2d9;
    --pill-text: #3d5a2c;
    --panel-grey: #efefef;
    --nav-grey: #666666;
    --body-grey: #555555;
    --dark-button: #333333;
    --footer-black: #050505;
    --footer-grey: #9a9a9a;
    --white: #ffffff;
    --pack-green: #5f9a45;
    --pack-red: #c9464a;
    --pack-orange: #e39a3a;
  }
  * { box-sizing: border-box; margin: 0; padding: 0; }
  html, body { width: 1200px; height: 1000px; overflow: hidden; background: var(--white); }
  body { position: relative; font-family: "Roboto", Arial, sans-serif; }

  .site-header {
    position: absolute; left: 0; top: 0; width: 1200px; height: 83px;
    background: linear-gradient(90deg, #ffffff 0%, #f4f4f4 50%, #e6e6e6 100%);
    border-bottom: 1px solid #d9d9d9;
  }
  .brand {
    position: absolute; left: 248px; top: 22px;
    display: flex; align-items: center; gap: 10px;
    font-family: "Roboto Condensed", Arial, sans-serif; font-weight: 700;
    font-size: 34px; color: var(--brand-green); letter-spacing: 1px;
  }
  .brand-dot { width: 12px; height: 12px; border-radius: 50%; background: var(--accent-green); }
  .main-nav a {
    position: absolute; top: 41px; white-space: nowrap; text-decoration: none;
    font-size: 12px; font-weight: 700; color: var(--nav-grey);
  }
  .main-nav a.is-current { color: var(--accent-green); }

  .hero {
    position: absolute; left: 0; top: 84px; width: 1200px; height: 326px;
    background:
      radial-gradient(ellipse 300px 140px at 130px 270px, rgba(20,70,20,.55), transparent),
      radial-gradient(ellipse 260px 120px at 1050px 60px, rgba(20,70,20,.5), transparent),
      radial-gradient(ellipse 500px 200px at 600px 160px, var(--hero-mid), transparent),
      linear-gradient(180deg, var(--hero-light) 0%, var(--hero-mid) 40%, var(--hero-dark) 100%);
  }
  .hero-title {
    position: absolute; left: 256px; top: 151px;
    font-family: "Roboto Condensed", Arial, sans-serif; font-weight: 700;
    font-size: 31px; color: var(--white);
  }
  .hero-tagline {
    position: absolute; left: 292px; top: 194px;
    font-family: "Roboto Condensed", Arial, sans-serif; font-weight: 700;
    font-size: 29px; color: var(--trust-yellow);
  }
  .hero-copy {
    position: absolute; left: 260px; top: 232px; width: 405px;
    font-family: "Roboto Condensed", Arial, sans-serif;
    font-size: 10.5px; line-height: 24px; color: var(--white); text-transform: uppercase;
  }
  .pill-button {
    position: absolute; display: flex; align-items: center; justify-content: center;
    background: var(--pill-green); border: 2px solid var(--pill-border); border-radius: 15px;
    font-family: "Roboto Condensed", Arial, sans-serif; color: var(--pill-text);
    box-shadow: 0 1px 3px rgba(0,0,0,.25);
  }
  .hero-button { left: 410px; top: 298px; width: 101px; height: 31px; font-size: 14px; }
  .hero-pack {
    position: absolute; left: 773px; top: 142px; width: 222px; height: 285px;
    background: linear-gradient(180deg, #f6f6f2 0%, var(--pack-green) 100%);
    box-shadow: 0 2px 6px rgba(0,0,0,.35);
  }

  .welcome-panel {
    position: absolute; left: 235px; top: 462px; width: 770px; height: 121px;
    background: var(--panel-grey); border-top: 2px solid var(--rule-green);
  }
  .welcome-title {
    position: absolute; left: 15px; top: 8px;
    font-family: "Roboto Condensed", Arial, sans-serif; font-weight: 700; font-size: 14px; color: #111;
  }
  .welcome-title span, .section-title span { color: var(--brand-green); }
  .welcome-copy {
    position: absolute; left: 13px; top: 31px; width: 720px;
    font-family: "Roboto Condensed", Arial, sans-serif; font-size: 10px; line-height: 18px; color: var(--body-grey);
  }
  .welcome-button { left: 664px; top: 85px; width: 87px; height: 26px; font-size: 12px; }
  .panel-shadow {
    position: absolute; height: 14px;
    background: radial-gradient(ellipse 50% 100% at 50% 0%, rgba(0,0,0,.22), transparent 70%);
  }

  .section-title {
    position: absolute; left: 234px; top: 615px;
    font-family: "Roboto Condensed", Arial, sans-serif; font-weight: 700; font-size: 14px; color: #111;
  }
  .section-rule { position: absolute; left: 234px; top: 630px; width: 767px; height: 2px; background: var(--rule-green); }

  .product-card { position: absolute; top: 642px; width: 235px; height: 258px; background: var(--panel-grey); }
  .product-pack { position: absolute; left: 52px; top: 9px; width: 123px; height: 160px; box-shadow: 0 1px 4px rgba(0,0,0,.3); }
  .pack-raspberry { background: linear-gradient(180deg, #f6f2f2 0%, var(--pack-red) 100%); }
  .pack-coffee { background: linear-gradient(180deg, #f2f6f1 0%, var(--pack-green) 100%); }
  .pack-garcinia { background: linear-gradient(180deg, #f7f3ec 0%, var(--pack-orange) 100%); }
  .product-copy {
    position: absolute; left: 13px; top: 184px; width: 222px;
    font-family: "Roboto Condensed", Arial, sans-serif; font-size: 9.5px; line-height: 15px; color: #333;
    white-space: nowrap;
  }
  .dark-button {
    position: absolute; left: 72px; top: 230px; width: 83px; height: 23px;
    display: flex; align-items: center; justify-content: center;
    background: var(--dark-button); color: var(--white);
    font-family: "Roboto Condensed", Arial, sans-serif; font-size: 13px;
  }

  .site-footer { position: absolute; left: 0; top: 921px; width: 1200px; height: 79px; background: var(--footer-black); }
  .footer-nav a {
    position: absolute; top: 40px; text-decoration: none; white-space: nowrap;
    font-size: 11px; font-weight: 700; color: var(--white);
  }
  .copyright { position: absolute; left: 831px; top: 38px; font-size: 11px; font-weight: 700; color: var(--footer-grey); }
</style>
</head>
<body>
  <header class="site-header">
    <div class="brand"><span>MEADOW VY</span><span class="brand-dot"></span></div>
    <nav class="main-nav">
      <a class="is-current" style="left:697px">HOME</a>
      <a style="left:767px">ABOUT US</a>
      <a style="left:850px">PRODUCT</a>
      <a style="left:923px">CONTACT US</a>
    </nav>
  </header>

  <section class="hero" role="img" aria-label="Blurred green garden background"></section>
  <h1 class="hero-title">THE BEST OF MEADOW VY TM</h1>
  <p class="hero-tagline">A BRAND YOU CAN TRUST</p>
  <p class="hero-copy">New Meadow Vy is line of natural, high-quality, weight-loss supplements that<br>are scientifically formulated for better efficacy!</p>
  <a class="pill-button hero-button">RAED MORE</a>
  <div class="hero-pack" role="img" aria-label="Product photo of a green coffee bean supplement box"></div>

  <section class="welcome-panel">
    <h2 class="welcome-title">WELCOME TO <span>MEADOW VY</span></h2>
    <p class="welcome-copy">Meadow Vy Green Coffee Bean is made with 100% pure natural ingredients. Unlike other products, Meadow Vy Green Coffee Bean is made with premium green coffee bean that<br>supplies 45% chlorogenic acid, which is the active weight-loss component of green coffee bean.</p>
    <a class="pill-button welcome-button">RAED MORE</a>
  </section>
  <div class="panel-shadow" style="left:235px;top:584px;width:770px"></div>

  <h2 class="section-title">OUR <span>PRODUCTS</span></h2>
  <div class="section-rule"></div>

  <article class="product-card" style="left:235px">
    <div class="product-pack pack-raspberry" role="img" aria-label="Product photo of a raspberry ketone supplement box"></div>
    <p class="product-copy">Meadow Vy Raspberry Ketone is made with 100% pure<br>raspberry ketone along with natural premium green tea.</p>
    <a class="dark-button">READ MORE</a>
  </article>
  <article class="product-card" style="left:501px">
    <div class="product-pack pack-coffee" role="img" aria-label="Product photo of a green coffee bean supplement box"></div>
    <p class="product-copy">Meadow Vy Raspberry Ketone is made with 100% pure<br>raspberry ketone along with natural premium green tea.</p>
    <a class="dark-button">READ MORE</a>
  </article>
  <article class="product-card" style="left:768px">
    <div class="product-pack pack-garcinia" role="img" aria-label="Product photo of a garcinia cambogia supplement box"></div>
    <p class="product-copy" style="top:183px">Meadow Vy Raspberry Ketone is made with 100% pure<br>raspberry ketone along with natural premium green tea.</p>
    <a class="dark-button" style="top:228px">READ MORE</a>
  </article>
  <div class="panel-shadow" style="left:235px;top:900px;width:235px"></div>
  <div class="panel-shadow" style="left:501px;top:900px;width:235px"></div>
  <div class="panel-shadow" style="left:768px;top:900px;width:235px"></div>

  <footer class="site-footer">
    <nav class="footer-nav">
      <a style="left:241px">HOME</a>
      <a style="left:311px">ABOUT US</a>
      <a style="left:394px">PRODUCT</a>
      <a style="left:468px">CONTACT US</a>
    </nav>
    <p class="copyright">Copyright © 2014 Meadow Vy.</p>
  </footer>
</body>
</html>
```